Need help in designing new business card utilizing our new logo.

BuildMarq Solutions works with Construction Business Owners, Managers & IT Professionals to strengthen software usage and increase user productivity.

Our Construction Accounting and Mobile Field Management Software Clients engage with us in the following areas:

New Software Implementations
Software Re-Implementations
Redesigning Software Usage at the User Level
Project Coordination & Management
Continued Software Support

Old tag line:
Weighing Options - Implementing Solutions

www.buildmarq-solutions.example

Stride 4 is a product, but not needed for a new business card.

```html
<!DOCTYPE html>
<html lang="en">
<head>
<meta charset="utf-8">
<title>BuildMarq Solutions – Business Card</title>
<link rel="stylesheet" href="https://fonts.googleapis.com/css2?family=Mulish:wght@400;600;700&display=swap">
<style>
  :root {
    --backdrop: #4f9e90;
    --card: #000000;
    --accent-red: #e8202a;
    --brand-blue: #33369a;
    --text-light: #ffffff;
  }
  html, body {
    margin: 0;
    padding: 0;
    width: 1200px;
    height: 900px;
    overflow: hidden;
    background: var(--backdrop);
    font-family: "Mulish", sans-serif;
  }
  .canvas {
    position: relative;
    width: 1200px;
    height: 900px;
  }
  .card {
    position: absolute;
    width: 528px;
    height: 292px;
    background: var(--card);
    color: var(--text-light);
    overflow: hidden;
  }

  /* Front */
  .card--front { left: 100px; top: 112px; }
  .front__rule {
    position: absolute;
    left: 0;
    width: 100%;
    height: 4px;
    background: var(--accent-red);
  }
  .front__rule--top { top: 14px; }
  .front__rule--bottom { top: 268px; }
  .front__brand {
    position: absolute;
    top: 124px;
    left: 0;
    width: 100%;
    text-align: center;
    color: var(--brand-blue);
    font-weight: 700;
    font-size: 26px;
    letter-spacing: 1px;
    text-transform: uppercase;
  }
  .front__web {
    position: absolute;
    top: 210px;
    left: 0;
    width: 100%;
    text-align: center;
    font-weight: 600;
    font-size: 13px;
    letter-spacing: 0.6px;
  }

  /* Back */
  .card--back { left: 550px; top: 438px; }
  .back__brand {
    position: absolute;
    left: 0;
    top: 132px;
    width: 199px;
    text-align: center;
    color: var(--brand-blue);
    font-weight: 700;
    font-size: 24px;
  }
  .back__band {
    position: absolute;
    left: 199px;
    top: 0;
    width: 28px;
    height: 100%;
    background: var(--accent-red);
  }
  .back__icon {
    position: absolute;
    left: 203px;
    width: 20px;
    height: 20px;
  }
  .back__icon--phone { top: 100px; }
  .back__icon--mail { top: 164px; }
  .back__icon--pin { top: 224px; }
  .back__name {
    position: absolute;
    top: 20px;
    left: 258px;
    right: 24px;
    text-align: center;
    font-weight: 700;
    font-size: 22px;
    letter-spacing: 1.5px;
    text-transform: uppercase;
  }
  .back__role {
    position: absolute;
    top: 50px;
    left: 258px;
    right: 24px;
    text-align: center;
    font-weight: 600;
    font-size: 13px;
    letter-spacing: 0.8px;
  }
  .back__detail {
    position: absolute;
    left: 258px;
    font-weight: 600;
    font-size: 12.5px;
    letter-spacing: 0.6px;
    line-height: 19px;
    margin: 0;
  }
  .back__detail--phone { top: 98px; }
  .back__detail--mail { top: 164px; }
  .back__detail--address { top: 224px; line-height: 11px; }
</style>
</head>
<body>
<main class="canvas">

  <section class="card card--front" aria-label="Card front">
    <div class="front__rule front__rule--top"></div>
    <div class="front__brand">BuildMarq Solutions</div>
    <div class="front__web">www.buildmarq-solutions.example</div>
    <div class="front__rule front__rule--bottom"></div>
  </section>

  <section class="card card--back" aria-label="Card back">
    <div class="back__brand">BuildMarq</div>
    <div class="back__band"></div>

    <svg class="back__icon back__icon--phone" viewBox="0 0 24 24" aria-hidden="true">
      <path d="M6.6 3.5l2.6 3.4-1.6 2.2c1.2 2.6 3.2 4.6 5.8 5.8l2.2-1.6 3.4 2.6-1.6 3.2C10.7 19 5 13.3 4.9 5.1z" fill="#fff"/>
      <path d="M14 3.5a6.5 6.5 0 0 1 6.5 6.5M14 6.5a3.5 3.5 0 0 1 3.5 3.5" stroke="#fff" stroke-width="1.8" fill="none" stroke-linecap="round"/>
    </svg>
    <svg class="back__icon back__icon--mail" viewBox="0 0 24 24" aria-hidden="true">
      <rect x="2.5" y="5.5" width="19" height="13" fill="#fff"/>
      <path d="M2.5 5.5l9.5 7.5 9.5-7.5M2.5 18.5l7-6M21.5 18.5l-7-6" stroke="#e8202a" stroke-width="1.4" fill="none"/>
    </svg>
    <svg class="back__icon back__icon--pin" viewBox="0 0 24 24" aria-hidden="true">
      <path d="M12 2a7 7 0 0 0-7 7c0 5 7 13 7 13s7-8 7-13a7 7 0 0 0-7-7z" fill="#fff"/>
      <circle cx="12" cy="9" r="2.6" fill="#e8202a"/>
    </svg>

    <div class="back__name">Dana R. Whitlock</div>
    <div class="back__role">Owner</div>
    <p class="back__detail back__detail--phone">800-555-0142 ext. 100<br>518-555-0193</p>
    <p class="back__detail back__detail--mail">dana@buildmarq-solutions.example</p>
    <p class="back__detail back__detail--address">14B Harbor Lane - PMB 118<br>Millbrook NY 12545</p>
  </section>

</main>
</body>
</html>
```